Anzeigengestaltung für Immobilienmakler
Zielgruppe
Wir sind ein Immobilienmakler. Wir wollen eine Plakatkampagne starten. Dazu brauchen wir ein Plakat.
Ich habe noch ein Foto des Plakats hochgeladen, um die Situation zu verdeutlichen.
Aufgabenstellung
Die Maße sind als Anhang dabei. Außerdem dabei ist ein Beispiel eines unserer Werbeschilder (daraus bitte die Farbgebung übernehmen), sowie unser Logo.
Das Plakat sollte mit einem Spruch sein, gerne mit Witz, pfiffig - einfach ein Hingucker.

```html
<!DOCTYPE html>
<html lang="de">
<head>
<meta charset="utf-8">
<title>Lena Hartwig Immobilien – Plakat</title>
<link href="https://fonts.googleapis.com/css2?family=Barlow:wght@300;400;500;600;700&family=Montserrat:wght@700&display=swap" rel="stylesheet">
<style>
  :root {
    --dark: #25272c;
    --tan: #bdb39b;
    --tan-deep: #a99d83;
    --light: #f2efe9;
    --ink: #2a2b30;
    --stage: #d9d9d9;
  }
  html, body {
    margin: 0;
    width: 831px;
    height: 1200px;
    overflow: hidden;
    background: var(--stage);
  }
  .poster-frame {
    position: absolute;
    left: 20px;
    top: 325px;
    width: 791px;
    height: 550px;
    overflow: hidden;
  }
  .poster {
    position: absolute;
    left: 0;
    top: 0;
    width: 1392px;
    height: 968px;
    transform: scale(0.5683);
    transform-origin: 0 0;
    background: var(--light);
    font-family: "Barlow", sans-serif;
    color: var(--ink);
  }
  .shapes { position: absolute; inset: 0; }
  .photo {
    position: absolute;
    inset: 0;
    background:
      radial-gradient(ellipse at 78% 45%, #e9edf1 0%, rgba(233,237,241,0) 45%),
      linear-gradient(90deg, #7c6a45 0%, #a89a7c 22%, #dfe3e6 45%, #c8ced4 70%, #3b3d42 100%);
    clip-path: polygon(744px 0, 1392px 0, 1392px 817px, 792px 817px, 930px 525px);
  }
  .brand {
    position: absolute;
    left: 70px;
    top: 88px;
    display: flex;
    align-items: center;
    gap: 34px;
  }
  .brand-square {
    width: 96px;
    height: 96px;
    background: var(--dark);
  }
  .brand-name {
    font-weight: 500;
    color: var(--dark);
    letter-spacing: 4px;
    line-height: 1;
  }
  .brand-name .name { display: block; font-size: 62px; }
  .brand-name .trade { display: block; font-size: 30px; letter-spacing: 9px; margin-top: 14px; padding-left: 116px; }
  .headline {
    position: absolute;
    left: 68px;
    top: 278px;
    margin: 0;
    color: var(--light);
    line-height: 0.92;
    font-size: 90px;
    letter-spacing: 2px;
  }
  .headline .light { display: block; font-weight: 400; }
  .headline .bold { display: block; font-weight: 700; }
  .tagline {
    position: absolute;
    left: 68px;
    top: 503px;
    margin: 0;
    font-size: 58px;
    font-weight: 400;
    letter-spacing: 1px;
    color: var(--dark);
  }
  .tagline strong { font-weight: 700; }
  .stats {
    position: absolute;
    left: 55px;
    top: 615px;
    display: flex;
  }
  .stat {
    text-align: center;
    padding: 0 12px;
    border-left: 2px solid #cfc8b8;
  }
  .stat:first-child { border-left: none; }
  .stat svg { display: block; margin: 0 auto; height: 72px; }
  .stat-number {
    font-family: "Montserrat", sans-serif;
    font-weight: 700;
    font-size: 35px;
    margin-top: 24px;
    line-height: 1;
  }
  .stat-label {
    font-size: 18px;
    line-height: 1.25;
    letter-spacing: 0.5px;
    margin-top: 6px;
    text-transform: uppercase;
    white-space: nowrap;
  }
  .phone {
    position: absolute;
    left: 90px;
    top: 862px;
    display: flex;
    align-items: center;
    gap: 30px;
    color: var(--light);
    font-weight: 700;
    font-size: 74px;
    letter-spacing: 4px;
    line-height: 1;
  }
  .web {
    position: absolute;
    left: 870px;
    top: 866px;
    display: flex;
    align-items: center;
    gap: 14px;
    font-weight: 600;
    font-size: 41px;
    color: var(--ink);
    line-height: 1;
  }
</style>
</head>
<body>
<div class="poster-frame">
  <div class="poster">
    <svg class="shapes" viewBox="0 0 1392 968" width="1392" height="968" aria-hidden="true">
      <polygon points="680,0 744,0 958,527 830,817 760,817 898,527" fill="var(--tan)"/>
      <polygon points="0,250 800,250 912,483 0,483" fill="var(--dark)"/>
      <polygon points="800,250 830,250 942,483 912,483" fill="var(--tan-deep)"/>
      <polygon points="0,483 912,483 930,527 900,590 0,590" fill="var(--tan)"/>
      <polygon points="0,590 858,590 748,835 0,835" fill="var(--light)"/>
      <polygon points="0,835 748,835 826,968 0,968" fill="var(--dark)"/>
      <polygon points="792,817 1392,817 1392,968 880,968" fill="var(--light)"/>
      <polygon points="740,835 792,817 880,968 826,968" fill="var(--tan)"/>
    </svg>

    <div class="photo" role="img" aria-label="Foto: Maklerin im Anzug bespricht mit einem jungen Paar Unterlagen auf einem Klemmbrett in einer hellen Wohnung"></div>

    <div class="brand">
      <div class="brand-square"></div>
      <div class="brand-name">
        <span class="name">LENA HARTWIG</span>
        <span class="trade">IMMOBILIEN</span>
      </div>
    </div>

    <h1 class="headline">
      <span class="light">WENN ES UM IHRE</span>
      <span class="bold">IMMOBILIE GEHT</span>
    </h1>

    <p class="tagline">SIND WIR DIE <strong>RICHTIGEN FÜR SIE</strong></p>

    <div class="stats">
      <div class="stat">
        <svg viewBox="0 0 72 72"><circle cx="36" cy="36" r="29" fill="none" stroke="var(--ink)" stroke-width="6"/><path d="M36 20v17l10 10" fill="none" stroke="var(--ink)" stroke-width="6" stroke-linecap="round"/></svg>
        <div class="stat-number">1997</div>
        <div class="stat-label">Langjährige<br>Erfahrung seit</div>
      </div>
      <div class="stat">
        <svg viewBox="0 0 80 72"><path d="M6 14h24l7 8h37v40H6z" fill="none" stroke="var(--ink)" stroke-width="5" stroke-linejoin="round"/></svg>
        <div class="stat-number">4021</div>
        <div class="stat-label">Kaufinteressenten<br>für Ihre Immobilie</div>
      </div>
      <div class="stat">
        <svg viewBox="0 0 80 72"><rect x="24" y="20" width="32" height="28" fill="none" stroke="var(--ink)" stroke-width="4"/><path d="M24 30h32M40 20v10" stroke="var(--ink)" stroke-width="4"/><path d="M12 66l8-18 4-28M68 66l-8-18-4-28" fill="none" stroke="var(--ink)" stroke-width="4" stroke-linecap="round"/></svg>
        <div class="stat-number">500+</div>
        <div class="stat-label">Abgeschlossene<br>Finanzierungen</div>
      </div>
      <div class="stat">
        <svg viewBox="0 0 72 72"><path d="M36 36c-9-7-16-12-16-19 0-5 4-8 8-8 4 0 6 2 8 5 2-3 4-5 8-5 4 0 8 3 8 8 0 7-7 12-16 19z" fill="none" stroke="var(--ink)" stroke-width="4" stroke-linejoin="round"/><path d="M8 50h14l10 6h14l18-10" fill="none" stroke="var(--ink)" stroke-width="4" stroke-linecap="round" stroke-linejoin="round"/><rect x="4" y="46" width="8" height="20" fill="none" stroke="var(--ink)" stroke-width="4"/></svg>
        <div class="stat-number">1510</div>
        <div class="stat-label">Glückliche<br>Kunden</div>
      </div>
    </div>

    <div class="phone">
      <svg width="30" height="52" viewBox="0 0 30 52" aria-hidden="true"><rect x="2" y="2" width="26" height="48" rx="5" fill="none" stroke="var(--light)" stroke-width="4"/><rect x="2" y="40" width="26" height="10" rx="4" fill="var(--light)"/></svg>
      <span>07031 4928160</span>
    </div>

    <div class="web">
      <svg width="30" height="30" viewBox="0 0 30 30" aria-hidden="true"><path d="M28 2L2 13l10 4 4 11z" fill="var(--ink)"/></svg>
      <span>LHartwig-immobilien.de</span>
    </div>
  </div>
</div>
</body>
</html>
```